Vornel Technologies business card design

We need a business card designed with our new logo. it would be great if the card could communicate it is a technology based company.

Target Market(s)

system integrators

Industry/Entity Type

technology, IOT

Contact Information for Business Card

Name, designation, Address, telephone number, email address

Requirements
Must have
• logo and company name
Nice to have
• something to do with technology

```html
<!DOCTYPE html>
<html lang="en">
<head>
<meta charset="UTF-8">
<title>Vornel Technologies — Business Card</title>
<link rel="stylesheet" href="https://fonts.googleapis.com/css2?family=Jost:wght@400;500;700&display=swap">
<style>
  :root {
    --backdrop: #4f5d79;
    --card-front: #252525;
    --card-back: #1f1f1f;
    --ink-light: #e6e6e6;
    --ink-muted: #c4c4c4;
    --accent: #e08a1e;
    --emboss: #111111;
  }
  * { margin: 0; padding: 0; box-sizing: border-box; }
  html, body {
    width: 1200px;
    height: 1000px;
    overflow: hidden;
    background: var(--backdrop);
    font-family: "Jost", "Futura", sans-serif;
  }
  .canvas {
    width: 1200px;
    height: 1000px;
    display: flex;
    flex-direction: column;
    align-items: center;
    justify-content: center;
    gap: 60px;
  }
  .card {
    width: 735px;
    height: 420px;
    border-radius: 4px;
    box-shadow: 0 12px 30px rgba(0, 0, 0, 0.3);
    position: relative;
  }
  .card--front {
    background: var(--card-front);
    display: flex;
    align-items: center;
    padding: 0 60px 0 80px;
  }
  .brand-mark {
    width: 260px;
    display: flex;
    align-items: center;
    gap: 14px;
  }
  .brand-mark__square {
    width: 22px;
    height: 22px;
    background: var(--accent);
    flex: none;
  }
  .brand-mark__name {
    color: var(--ink-light);
    font-weight: 500;
    font-size: 44px;
    letter-spacing: 1px;
  }
  .contact {
    margin-left: 60px;
    color: var(--ink-muted);
  }
  .contact__name {
    color: var(--ink-light);
    font-weight: 400;
    font-size: 34px;
    letter-spacing: 2px;
    line-height: 1;
  }
  .contact__title {
    color: var(--accent);
    font-size: 17px;
    letter-spacing: 1.5px;
    margin-top: 6px;
  }
  .contact__email {
    font-size: 17px;
    letter-spacing: 1.5px;
    margin-top: 30px;
  }
  .contact__lines {
    margin-top: 26px;
    font-size: 17px;
    letter-spacing: 1.5px;
    line-height: 1.5;
    font-style: normal;
  }
  .card--back {
    background: var(--card-back);
    display: flex;
    align-items: center;
    justify-content: center;
  }
  .back-wordmark {
    color: var(--emboss);
    font-weight: 700;
    font-size: 58px;
    letter-spacing: 4px;
    text-transform: uppercase;
    text-align: center;
    line-height: 1.1;
  }
</style>
</head>
<body>
  <main class="canvas">
    <section class="card card--front" aria-label="Business card front">
      <div class="brand-mark">
        <span class="brand-mark__square"></span>
        <span class="brand-mark__name">Vornel</span>
      </div>
      <div class="contact">
        <h1 class="contact__name">DARIO LENKO</h1>
        <p class="contact__title">Progamer Director</p>
        <p class="contact__email">dario@vornel.com</p>
        <address class="contact__lines">
          +123 456 780 115<br>
          123. Main Street, City, State
        </address>
      </div>
    </section>
    <section class="card card--back" aria-label="Business card back">
      <p class="back-wordmark">Vornel<br>Technologies</p>
    </section>
  </main>
</body>
</html>
```